Brochure for International and Domestic Festival & Music Student Tour Company

We need a brochure for our Festival and Music Student Tour Company. Brochure needs to communicate clearly what we offer. It should be visually exciting and inspirational. We want to see our brand colors incorporated as well as the swoosh (I will provide image) we use on our other marketing materials. Think outside the box, we don't want a standard template. This needs to stand out and make people want to read it. Imagery is important. I have provided the content in a word document as well as images and logos. Harborlight Journey Tours is the main logo but we also need to include the Pellwick Tours logo (smaller) and the Family of Logos should be with the address. All these will be provided to you.

Target Market(s)

Music Directors - Middle School, High School, and College

Industry/Entity Type

Tourism

Font styles to use
Serif
Sans Serif

Requirements
Must have
• Our logos

```html
<!DOCTYPE html>
<html lang="en">
<head>
<meta charset="utf-8">
<title>Harborlight Journey Tours – Brochure Spread</title>
<link href="https://fonts.googleapis.com/css2?family=Lato:ital,wght@0,400;0,700;0,900;1,400;1,700;1,900&display=swap" rel="stylesheet">
<style>
  :root {
    --backdrop: #2b2b2d;
    --paper: #eceef6;
    --navy: #2c2f78;
    --ink: #33344a;
    --red: #b3131c;
    --grey-bubble: #6b6d73;
    --violet-bubble: #4b4a8e;
    --white: #ffffff;
    --sky: #6fa6e8;
    --blue: #2d67d2;
    --deep-blue: #1b3596;
    --crimson: #b2141b;
    --maroon: #620a0e;
  }
  * { box-sizing: border-box; margin: 0; padding: 0; }
  html, body { width: 1200px; height: 789px; overflow: hidden; }
  body {
    background: var(--backdrop);
    font-family: "Lato", sans-serif;
    position: relative;
  }
  .spread {
    position: absolute;
    left: 60px; top: 45px;
    width: 1080px; height: 700px;
    display: flex;
  }
  .page { position: relative; width: 540px; height: 700px; overflow: hidden; }

  /* ---------- Left page ---------- */
  .page--tours { background: var(--paper); color: var(--ink); }
  .heading {
    font-style: italic; font-weight: 900; color: var(--navy);
    position: absolute; left: 36px;
  }
  .tours-title { top: 34px; font-size: 30px; }
  .small-copy { position: absolute; font-size: 10px; line-height: 1.3; font-style: italic; }
  .mission { left: 36px; top: 78px; width: 250px; font-weight: 700; }
  .priorities { left: 36px; top: 112px; width: 240px; }
  .priorities strong { display: block; }
  .bullets { position: absolute; list-style: none; }
  .bullets li {
    position: relative; padding-left: 14px;
    font-size: 11px; font-weight: 700; font-style: italic; line-height: 1.45;
  }
  .bullets li::before {
    content: ""; position: absolute; left: 0; top: 5px;
    width: 5px; height: 5px; border-radius: 50%; background: var(--red);
  }
  .tour-bullets { left: 36px; top: 170px; }

  .photo { position: absolute; }
  .photo--round { border-radius: 50%; }
  .skyline-arc {
    left: 350px; top: 18px; width: 320px; height: 320px;
    border-left: 14px solid var(--navy);
    background: linear-gradient(160deg, #b9d3ea 0%, #7ea6c9 45%, #4b7a7a 70%, #344b5e 100%);
  }
  .ring-red { border: 5px solid var(--red); box-shadow: 0 0 0 3px var(--paper); }
  .ring-navy { border: 5px solid var(--navy); box-shadow: 0 0 0 3px var(--paper); }
  .colosseum { left: 290px; top: 92px; width: 112px; height: 112px;
    background: linear-gradient(170deg, #8fb4de 0%, #c9a067 55%, #8a5f32 100%); }
  .bridge { left: 240px; top: 205px; width: 88px; height: 88px;
    background: linear-gradient(170deg, #e2b37a 0%, #6d87b5 50%, #24406e 100%); }
  .cathedral { left: 318px; top: 182px; width: 128px; height: 128px;
    background: linear-gradient(170deg, #9fc1e6 0%, #b89a70 55%, #5a6a3a 100%); }

  .quote {
    position: absolute; color: var(--white);
    font-size: 10px; font-style: italic; line-height: 1.35;
  }
  .quote__mark { position: absolute; font-family: Georgia, serif; font-size: 64px; font-weight: 700; line-height: 1; }
  .quote--grey {
    left: 28px; top: 300px; width: 484px; height: 92px;
    background: var(--grey-bubble); border-radius: 22px 22px 22px 22px;
    padding: 16px 60px 0 74px;
  }
  .quote--grey .quote__mark--open { left: 14px; top: 4px; color: #d6d7db; }
  .quote--grey .quote__mark--close { right: 14px; bottom: -20px; color: var(--white); }
  .quote cite { display: block; text-align: right; font-weight: 700; margin-top: 3px; }

  .festivals-title { top: 408px; font-size: 28px; }
  .festival-copy {
    position: absolute; left: 36px; top: 448px; width: 470px;
    font-size: 11px; font-weight: 700; line-height: 1.35;
  }
  .festival-bullets { left: 36px; top: 500px; }

  .quote--violet {
    left: 345px; top: 505px; width: 175px; height: 105px;
    background: var(--violet-bubble); border-radius: 18px;
    padding: 14px 22px 0 44px;
  }
  .quote--violet .quote__mark--open { left: 8px; top: 2px; font-size: 48px; color: #c9c8e4; }
  .quote--violet .quote__mark--close { right: 10px; bottom: -16px; font-size: 48px; color: #c9c8e4; }

  .stage-costumes { left: 28px; top: 612px; width: 150px; height: 82px;
    background: linear-gradient(160deg, #1d2f5a 0%, #6a3a3a 60%, #c8a06a 100%); }
  .concert-hall { left: 186px; top: 616px; width: 160px; height: 80px;
    background: linear-gradient(180deg, #3a1d12 0%, #a26a2a 55%, #7a1b16 100%); }
  .orchestra { left: 354px; top: 618px; width: 160px; height: 78px;
    background: linear-gradient(160deg, #8f8f8f 0%, #3a3a3a 60%, #1a1a1a 100%); }

  /* ---------- Right page ---------- */
  .page--services {
    background: linear-gradient(176deg, var(--sky) 0%, var(--blue) 40%, var(--deep-blue) 60%, var(--crimson) 84%, var(--maroon) 100%);
    color: var(--white);
  }
  .facets { position: absolute; right: 0; top: 150px; }
  .services-title { position: absolute; left: 40px; top: 34px; font-size: 28px; font-weight: 900; font-style: italic; }
  .services-copy { position: absolute; left: 40px; top: 80px; width: 380px; }
  .services-copy p { font-size: 9.5px; line-height: 1.3; margin-bottom: 6px; opacity: .95; }
  .included-title { position: absolute; left: 40px; top: 326px; font-size: 26px; font-weight: 900; font-style: italic; }
  .included-col { position: absolute; }
  .included-col--left { left: 40px; top: 375px; width: 230px; }
  .included-col--right { left: 290px; top: 440px; width: 230px; }
  .included-group { margin-bottom: 16px; }
  .included-group h3 { font-size: 13px; font-weight: 900; font-style: italic; margin-bottom: 4px; }
  .included-group ul { list-style: none; }
  .included-group li { position: relative; padding-left: 12px; font-size: 9.5px; line-height: 1.4; }
  .included-group li::before {
    content: ""; position: absolute; left: 2px; top: 5px;
    width: 4px; height: 4px; border-radius: 50%; background: var(--white);
  }
</style>
</head>
<body>
<main class="spread">

  <section class="page page--tours">
    <div class="photo photo--round skyline-arc" role="img" aria-label="Photo of the Statue of Liberty and New York skyline"></div>
    <div class="photo photo--round ring-red colosseum" role="img" aria-label="Photo of the Colosseum in Rome"></div>
    <div class="photo photo--round ring-navy bridge" role="img" aria-label="Photo of the Golden Gate Bridge at sunset"></div>
    <div class="photo photo--round ring-red cathedral" role="img" aria-label="Photo of a Gothic cathedral in Paris"></div>

    <h1 class="heading tours-title">Our Tours:</h1>
    <p class="small-copy mission">Our Mission is to showcase the performing arts at home and abroad.</p>
    <p class="small-copy priorities"><strong>Our priorities:</strong>To address the unique needs of performing groups, to provide the right mix of sightseeing, cultural immersion &amp; performance.</p>
    <ul class="bullets tour-bullets">
      <li>Domestic &amp; International Destinations</li>
      <li>Customized Itineraries</li>
      <li>Legendary Performance Venues</li>
      <li>Extensive Concert Promotion</li>
      <li>Knowledgeable Local Partners</li>
      <li>Inspiring Educational Experiences</li>
    </ul>

    <blockquote class="quote quote--grey">
      <span class="quote__mark quote__mark--open">“</span>
      My trips abroad with jazz bands have been worry free because of Harborlight Journey Tours' detailed planning, personal attention, outstanding service, quality accommodations, and great value.
      <cite>– Celia, Director, Ohio</cite>
      <span class="quote__mark quote__mark--close">”</span>
    </blockquote>

    <h2 class="heading festivals-title">Our Festivals:</h2>
    <p class="festival-copy">Harborlight Journey Tours &amp; Music Festivals provides exceptional festival experiences to thousands of elementary, middle school, and high school students in bands, choirs, and orchestras. Our festivals are conveniently located near popular attractions.</p>
    <ul class="bullets festival-bullets">
      <li>Exceptional Venues</li>
      <li>Distinctive Awards</li>
      <li>Competitive or Motivational Platform</li>
      <li>Professional Recordings</li>
      <li>Specialty Festivals for Developing Groups</li>
      <li>Outstanding Adjudicators &amp; Clinicians</li>
    </ul>

    <blockquote class="quote quote--violet">
      <span class="quote__mark quote__mark--open">“</span>
      It was a wonderful venue and a great event! The festival is an exceptional learning experience.
      <cite>– Renata, Director, Iowa</cite>
      <span class="quote__mark quote__mark--close">”</span>
    </blockquote>

    <div class="photo stage-costumes" role="img" aria-label="Photo of a costumed choir on stage"></div>
    <div class="photo concert-hall" role="img" aria-label="Photo of an ornate concert hall interior"></div>
    <div class="photo orchestra" role="img" aria-label="Photo of a student orchestra performing"></div>
  </section>

  <section class="page page--services">
    <svg class="facets" width="200" height="330" viewBox="0 0 200 330" aria-hidden="true">
      <polygon points="200,0 200,210 60,150" fill="#1b2f8c"/>
      <polygon points="200,0 60,150 150,165" fill="#2a4fb8" opacity=".8"/>
      <polygon points="60,150 200,210 200,330" fill="#3b6fd0" opacity=".55"/>
      <polygon points="150,165 200,210 60,150" fill="#15257a" opacity=".7"/>
    </svg>

    <h2 class="services-title">Our Services:</h2>
    <div class="services-copy">
      <p>We offer expertise, attention to detail, and a passion for providing the highest level of service in the industry.</p>
      <p>Our "travel you way" policy gives us the flexibility to design a trip that is aligned with your vision and exceptions.</p>
      <p>With over 100 years of combined experience working in student travel, our expertise provides you with unbeatable customer service.</p>
      <p>We are focused on providing your students with a culturally enriching, fun, and professionally managed experience at a cost which fits your budget.</p>
      <p>We strive to make every tour and music festival the best it can be. Our highly experienced staff takes the guesswork out of planning and guides you through every step of the process, providing you with unbeatable customer service.</p>
      <p>As members of the Youth Travel Guild and three national tour associations, we adhere to a strict set of ethical, financial, and professional standards.</p>
      <p>Student safety and well-being are our top priorities. Our TourLink mobile app features real time GPS tracking so tour guides and teachers can monitor students at all times. CareAway provides 24/7 medical care to all students while on tour.</p>
    </div>

    <h2 class="included-title">What's Included:</h2>
    <div class="included-col included-col--left">
      <div class="included-group">
        <h3>Itineraries</h3>
        <ul><li>Customized</li><li>Flexible</li><li>Expertly Planned</li></ul>
      </div>
      <div class="included-group">
        <h3>Safe, Quality Accommodations</h3>
        <ul><li>Wide range of choices</li><li>3-5 star hotels</li><li>Upscale youth hostels</li><li>Student residence halls</li></ul>
      </div>
      <div class="included-group">
        <h3>Efficient Transportation Arrangements</h3>
        <ul><li>Includes instrument transportation</li><li>Based on established relationships with providers</li><li>Both air and land included</li></ul>
      </div>
    </div>
    <div class="included-col included-col--right">
      <div class="included-group">
        <h3>Optimum Performance Arrangements</h3>
        <ul><li>Instrument/Equipment Coordination</li><li>Warm Up Provisions</li><li>Performance Setting/Acoustics</li></ul>
      </div>
      <div class="included-group">
        <h3>Varied Meal Arrangements</h3>
        <ul><li>Local cuisine</li><li>Hotel meals</li><li>Specialty restaurants</li></ul>
      </div>
      <div class="included-group">
        <h3>Comprehensive Online Tools</h3>
        <ul><li>Registration</li><li>Payments</li><li>Access to itinerary</li><li>Create, access rooming lists</li><li>View participants' payments/balance due</li></ul>
      </div>
    </div>
  </section>

</main>
</body>
</html>
```